Business card for Chiropractic clinics needs reworked / redesigned

The business card in attachment was designed 10 years ago. It is in need of an update.
We have 2 clinics:
VELDHOVE KLINIEK & VELDHOVE KLINIEK NOORD
Only one address needs to be on the card for doctors that only work in one clinic and two addresses need to be on the card for the doctors that work in both clinics.

Target Market(s)

patients/referrers

Industry/Entity Type

Medical

Contact Information for Business Card

Logo (in full or zoomed-in)
Clinic Name
Doctor name and title
clinic address, website, tel, email

Font styles to use
Sans Serif

Colors

Designer to choose colors to be used in the design.

Requirements
Must have
• Good contrast/readability
• We like modern minimalistic designs
• The Bcard needs to project our very high standard of proficiency/professionalism
Should not have
• Not curly
• Not to much colours

```html
<!DOCTYPE html>
<html lang="nl">
<head>
<meta charset="utf-8">
<title>Veldhove Kliniek – visitekaartje</title>
<link rel="stylesheet" href="https://fonts.googleapis.com/css2?family=Roboto+Condensed:wght@400;700&family=Open+Sans:wght@400;600&display=swap">
<style>
  :root {
    --backdrop: #2b3036;
    --green: #245a44;
    --green-deep: #1f4f3c;
    --blue: #4aaee3;
    --white: #ffffff;
    --paper: #f4f5f5;
    --ink: #2a2a2a;
    --muted: #cfe0d8;
  }
  * { box-sizing: border-box; margin: 0; padding: 0; }
  html, body { width: 1200px; height: 900px; overflow: hidden; background: var(--backdrop); }
  .canvas { position: relative; width: 1200px; height: 900px; }

  .card {
    position: absolute; left: 290px; width: 620px; height: 354px;
    border-radius: 4px; overflow: hidden;
    box-shadow: 0 18px 40px rgba(0,0,0,.45);
  }
  .card--back { top: 70px; background: linear-gradient(135deg, var(--green-deep), var(--green) 60%, #2b6650); }
  .card--front { top: 476px; background: linear-gradient(135deg, var(--white), var(--paper)); }

  .wordmark {
    position: absolute; font-family: "Roboto Condensed", sans-serif; font-weight: 700;
    letter-spacing: 1px; text-transform: uppercase; line-height: 1; white-space: nowrap;
  }
  .card--back .wordmark { left: 150px; top: 157px; font-size: 40px; color: var(--white); }
  .card--front .wordmark {
    left: 320px; width: 270px; top: 50%; transform: translateY(-50%);
    text-align: center; font-size: 28px; color: var(--ink);
  }

  .front-shape { position: absolute; inset: 0; }

  .details { position: absolute; left: 28px; top: 26px; color: var(--white); font-family: "Open Sans", sans-serif; }
  .doctor-name { font-family: "Roboto Condensed", sans-serif; font-weight: 700; font-size: 21px; letter-spacing: .5px; text-transform: uppercase; }
  .doctor-title { font-family: "Roboto Condensed", sans-serif; font-size: 15px; color: var(--blue); letter-spacing: 1px; margin-bottom: 18px; }
  .clinic { margin-bottom: 16px; }
  .clinic-name { font-family: "Roboto Condensed", sans-serif; font-weight: 700; font-size: 15px; text-transform: uppercase; letter-spacing: .5px; }
  .clinic-address { font-size: 11px; color: var(--muted); margin: 2px 0 5px; }
  .contact-line { display: flex; align-items: center; gap: 7px; font-size: 11px; margin-top: 3px; }
  .contact-icon { width: 13px; height: 13px; flex: none; }
</style>
</head>
<body>
<main class="canvas">

  <section class="card card--back" aria-label="Achterkant visitekaartje">
    <div class="wordmark">Veldhove Kliniek</div>
  </section>

  <section class="card card--front" aria-label="Voorkant visitekaartje">
    <svg class="front-shape" viewBox="0 0 620 354" width="620" height="354" aria-hidden="true">
      <path d="M0 0 H290 C225 90 330 215 262 354 H0 Z" fill="var(--green)"/>
      <path d="M290 0 C225 90 330 215 262 354" fill="none" stroke="var(--blue)" stroke-width="12"/>
    </svg>

    <div class="details">
      <div class="doctor-name">Maarten Verhaegen</div>
      <div class="doctor-title">CHIROPRACTOR</div>

      <div class="clinic">
        <div class="clinic-name">Veldhove Kliniek Noord</div>
        <div class="clinic-address">Kerkdreef 41</div>
        <div class="contact-line">
          <svg class="contact-icon" viewBox="0 0 14 14"><rect width="14" height="14" rx="3" fill="var(--blue)"/><path d="M4 3.5l1.6-.4 1 2.2-1 .8a5 5 0 0 0 2.3 2.3l.8-1 2.2 1-.4 1.6C7 10.3 3.7 7 4 3.5z" fill="var(--white)"/></svg>
          <span>09 555 18 42</span>
        </div>
        <div class="contact-line">
          <svg class="contact-icon" viewBox="0 0 14 14"><rect width="14" height="14" rx="3" fill="var(--blue)"/><circle cx="7" cy="7" r="4" fill="none" stroke="var(--white)" stroke-width="1"/><path d="M3 7h8M7 3c-2 2.5-2 5.5 0 8M7 3c2 2.5 2 5.5 0 8" fill="none" stroke="var(--white)" stroke-width=".8"/></svg>
          <span>veldhovenoord.be</span>
        </div>
      </div>

      <div class="clinic">
        <div class="clinic-name">Veldhove Kliniek</div>
        <div class="clinic-address">Lindenlaan 118</div>
        <div class="contact-line">
          <svg class="contact-icon" viewBox="0 0 14 14"><rect width="14" height="14" rx="3" fill="var(--blue)"/><path d="M4 3.5l1.6-.4 1 2.2-1 .8a5 5 0 0 0 2.3 2.3l.8-1 2.2 1-.4 1.6C7 10.3 3.7 7 4 3.5z" fill="var(--white)"/></svg>
          <span>09 555 70 31</span>
        </div>
        <div class="contact-line">
          <svg class="contact-icon" viewBox="0 0 14 14"><rect width="14" height="14" rx="3" fill="var(--blue)"/><circle cx="7" cy="7" r="4" fill="none" stroke="var(--white)" stroke-width="1"/><path d="M3 7h8M7 3c-2 2.5-2 5.5 0 8M7 3c2 2.5 2 5.5 0 8" fill="none" stroke="var(--white)" stroke-width=".8"/></svg>
          <span>veldhovekliniek.be</span>
        </div>
      </div>
    </div>

    <div class="wordmark">Veldhove Kliniek</div>
  </section>

</main>
</body>
</html>
```